Sign Advertisment for Condominium Development

I need a sign created that will be placed in front of a building that is being converted into a luxury condominium development.

The sign needs to say:

Two, Boutique Luxury Condominiums Delivering late 2015.

Luxury Finishes // Designer Kitchens and Bath // Each Unit over 2,000 Square Feet

Deeded Parking Included with Each Unit

To Learn More, Contact:

Loretta Pinwell or Morgan Tesh
(202) 555-0147
Loretta.Pinwell@nrg-example.com

I need a small disclaimer at the bottom stating:

These Condominium(s) have not been registered by the Office of Residential Property Oversight Bureau of Dwelling Registration Tenancy Transfer and Purchase Section. A Condominium Unit may be reserved on a non-binding reservation agreement, but no contract of sale or lease that is binding on the purchaser may be entered into prior to registration.

Target Market(s)

Young professionals seeking luxury condominium

Industry/Entity Type

Building

Font styles to use
Serif

Colors
00a88f
ffffff

```html
<!DOCTYPE html>
<html lang="en">
<head>
<meta charset="utf-8">
<title>Boutique Luxury Condominiums – Site Sign</title>
<link rel="stylesheet" href="https://fonts.googleapis.com/css2?family=Noto+Serif:wght@400;500;700&family=Arimo&display=swap">
<style>
  :root {
    --teal: #00a88f;
    --white: #ffffff;
    --ink: #333333;
    --frame: #b8b8b8;
    --hardware: #c9c9c9;
    --ornament: rgba(255, 255, 255, 0.3);
  }
  * { margin: 0; padding: 0; box-sizing: border-box; }
  html, body { width: 1126px; height: 1200px; overflow: hidden; background: var(--white); }
  .sheet {
    position: relative;
    width: 1126px;
    height: 1200px;
    border: 1px solid var(--frame);
    background: var(--white);
    font-family: "Noto Serif", Georgia, serif;
  }
  .sign-shape { position: absolute; left: 0; top: 0; }
  .line {
    position: absolute;
    left: 0;
    width: 1123px;
    text-align: center;
    color: var(--white);
    white-space: nowrap;
    line-height: 1;
  }
  .kicker   { top: 204px; font-size: 36px; font-weight: 500; }
  .headline { top: 262px; font-size: 70px; font-weight: 500; }
  .feature  { font-size: 47px; font-weight: 500; }
  .feature-1 { top: 398px; }
  .feature-2 { top: 459px; }
  .detail   { font-size: 36px; font-weight: 500; }
  .detail-1 { top: 528px; }
  .detail-2 { top: 574px; }
  .contact-label {
    position: absolute;
    left: 388px;
    top: 661px;
    width: 347px;
    height: 34px;
    background: var(--white);
    color: var(--ink);
    font-size: 19px;
    font-weight: 500;
    line-height: 34px;
    text-align: center;
    white-space: nowrap;
  }
  .contact { font-size: 21px; font-weight: 700; }
  .contact-names { top: 721px; }
  .contact-phone { top: 748px; }
  .contact-email { top: 775px; }
  .disclaimer {
    position: absolute;
    left: 246px;
    top: 832px;
    width: 630px;
    color: var(--white);
    font-size: 10.6px;
    line-height: 1.2;
    text-align: center;
  }
  .specs {
    position: absolute;
    left: 130px;
    top: 1038px;
    color: var(--ink);
    font-family: "Arimo", Arial, sans-serif;
  }
  .specs-title { font-size: 32px; line-height: 1.2; }
  .specs-item { font-size: 20px; line-height: 34px; }
</style>
</head>
<body>
<div class="sheet">
  <svg class="sign-shape" width="1126" height="1200" viewBox="0 0 1126 1200">
    <g class="panel" fill="var(--teal)">
      <rect x="134" y="117" width="855" height="852"/>
      <path d="M411 118 Q567 40 724 118 Z"/>
      <path d="M411 968 Q567 1050 724 968 Z"/>
    </g>
    <g class="rules" stroke="var(--white)" stroke-linecap="round" fill="none">
      <line x1="356" y1="160" x2="763" y2="160" stroke-width="4"/>
      <line x1="356" y1="926" x2="763" y2="926" stroke-width="4"/>
      <line x1="174" y1="346" x2="174" y2="748" stroke-width="4"/>
      <line x1="949" y1="346" x2="949" y2="748" stroke-width="4"/>
    </g>
    <g class="corner-ornaments" fill="var(--ornament)">
      <path role="img" aria-label="Decorative scroll flourish, top left corner" d="M160 148 H292 V188 H206 V300 H160 Z"/>
      <path role="img" aria-label="Decorative scroll flourish, top right corner" d="M948 148 H800 V188 H902 V300 H948 Z"/>
      <path role="img" aria-label="Decorative scroll flourish, bottom left corner" d="M160 928 H292 V890 H206 V778 H160 Z"/>
      <path role="img" aria-label="Decorative scroll flourish, bottom right corner" d="M948 928 H800 V890 H902 V778 H948 Z"/>
    </g>
    <g class="mounting-screws" fill="var(--hardware)">
      <circle cx="159" cy="142" r="12"/>
      <circle cx="958" cy="142" r="12"/>
      <circle cx="159" cy="946" r="12"/>
      <circle cx="958" cy="946" r="12"/>
    </g>
  </svg>

  <div class="line kicker">Boutique Luxury Condominiums</div>
  <div class="line headline">Delivering late 2015</div>

  <div class="line feature feature-1">Luxury Finishes</div>
  <div class="line feature feature-2">Designer Kitchens and Bath</div>
  <div class="line detail detail-1">Each Unit over 2,000 Square Feet</div>
  <div class="line detail detail-2">Deeded Parking Included with Each Unit</div>

  <div class="contact-label">TO LEARN MORE, CONTACT:</div>
  <div class="line contact contact-names">Loretta Pinwell or Morgan Tesh</div>
  <div class="line contact contact-phone">(202) 555-0147</div>
  <div class="line contact contact-email">Loretta.Pinwell@nrg-example.com</div>

  <p class="disclaimer">These Condominium(s) have not been registered by the Office of Residential Property Oversight Bureau of Dwelling Registration Tenancy Transfer and Purchase Section. A Condominium Unit may be reserved on a non-binding reservation agreement, but no contract of sale or lease that is binding on the purchaser may be entered into prior to registration.</p>

  <div class="specs">
    <div class="specs-title">Spesifications:</div>
    <div class="specs-item">size: 16” X 16” inch</div>
    <div class="specs-item">Material: Acrilic</div>
  </div>
</div>
</body>
</html>
```